3 fold Flyer Design (A4)

We are offering a good value, professional, Search Engine Optimisation package which is being offered with a 'free' entry onto a local web site. and need to advertise the benefits within a 3 fold flyer. The content may change to show the name of a differen local website (e.g. www.marshfieldhub.com . The design must look exciting, this is a great offer!

We have attached a draft of the content to the brief. A new brief has been atached 05/01/2011

Reason: Having viewed the existing designs we feel a need for change to a more dynamic 'sales' approach

Having reviewd the designs we decided to change our approah to make the brochure more sales led than professional.
To compensate for this we have increased the budget a little.
We have also added new text and improved the brief.
Thanks

Target Market(s)

business owners in the North West. Mostly private businesses from shops to manufacturing. Mostly in competitive markets.

Industry/Entity Type

It Professional

Requirements
Must have
• Bright fresh approach which gets over the benefit of increasing business. Happy and positive, with the concept of success.

The Brandon vale Internet logo added to the back page small in size. (attached)
Nice to have
• design which gives the reader confidence to buy
Should not have
• Boring pictures

```html
<!DOCTYPE html>
<html lang="en">
<head>
<meta charset="utf-8">
<title>SEO Tri-fold Flyer – Inside and Outside Spreads</title>
<link rel="stylesheet" href="https://fonts.googleapis.com/css2?family=PT+Sans:ital,wght@0,400;0,700;1,700&display=swap">
<style>
  :root {
    --stage: #1c1c1c;
    --paper: #ffffff;
    --ink: #5c5c5c;
    --ink-soft: #7a7a7a;
    --heading: #666a6c;
    --teal: #1f8d98;
    --teal-deep: #137580;
    --teal-dark: #0d5f68;
    --aqua: #bfe9f0;
    --aqua-soft: #e4f6f9;
    --rule: #9fd6e2;
    --pale-cyan: #b9ecf2;
    --white: #ffffff;
  }
  * { box-sizing: border-box; margin: 0; padding: 0; }
  html, body { width: 1200px; height: 1030px; overflow: hidden; background: var(--stage); }
  body { position: relative; font-family: "PT Sans", sans-serif; color: var(--ink); }

  .spread {
    position: absolute; left: 270px; width: 660px; height: 500px;
    background: var(--paper); overflow: hidden;
  }
  .spread--inside { top: 8px; }
  .spread--outside { top: 520px; }
  .abs { position: absolute; }

  /* soft aqua streaks across the top edge */
  .streak {
    position: absolute; left: 0; right: 0; top: 0; height: 70px;
    background: linear-gradient(180deg, var(--aqua) 0%, rgba(228,246,249,0.6) 45%, rgba(255,255,255,0) 100%);
  }
  .streak--right { background: linear-gradient(200deg, #a9e0ea 0%, rgba(228,246,249,0.5) 40%, rgba(255,255,255,0) 75%); }
  .column-wash {
    position: absolute; top: 0; bottom: 0; left: 0; width: 215px;
    background: linear-gradient(90deg, rgba(200,235,242,0.55), rgba(230,246,249,0.3) 60%, rgba(255,255,255,0));
  }

  /* inside spread */
  .site-title { left: 24px; top: 62px; font-size: 17px; font-weight: 700; color: #56808a; }
  .site-sub { left: 24px; top: 82px; font-size: 11.5px; font-weight: 700; line-height: 1.15; color: var(--ink); }
  .rule { height: 1px; background: var(--rule); }
  .body-copy { font-size: 8.3px; line-height: 1.38; color: var(--ink-soft); width: 180px; }
  .seo-title { left: 24px; top: 302px; font-size: 11.5px; font-weight: 700; line-height: 1.15; color: var(--ink); }
  .seo-title strong { font-size: 15px; }
  .panel-title { font-size: 17px; font-weight: 700; color: var(--heading); }
  .item-title { left: 456px; top: 62px; font-size: 7.6px; font-weight: 700; color: var(--ink); }

  /* outside spread */
  .value-title { left: 22px; top: 60px; font-size: 17px; font-weight: 700; color: var(--heading); }
  .value-copy { left: 23px; top: 90px; width: 190px; font-size: 9px; line-height: 1.3; color: var(--ink-soft); }
  .value-copy p + p { margin-top: 8px; }
  .value-copy .contact { color: var(--teal); }
  .photo-pen {
    left: 228px; top: 112px; width: 212px; height: 124px;
    background: linear-gradient(100deg, #f2f4f5 0%, #d8dcde 35%, #b9a79a 60%, #e6e9ea 100%);
  }
  .teal-band {
    left: 0; top: 236px; width: 456px; height: 264px;
    background: linear-gradient(180deg, var(--teal) 0%, #2a98a2 35%, var(--teal-deep) 62%, #2a8e98 75%, var(--teal-dark) 100%);
  }
  .band-lead { left: 24px; top: 262px; font-size: 7.8px; color: var(--pale-cyan); line-height: 1.25; width: 190px; }
  .band-small { left: 24px; top: 281px; font-size: 5.8px; color: #dff6f8; line-height: 1.3; width: 200px; }
  .band-note { left: 232px; top: 278px; width: 210px; text-align: center; font-size: 8.3px; font-weight: 700; color: var(--white); line-height: 1.25; }
  .band-note .ask { display: block; margin-top: 8px; color: var(--pale-cyan); }

  .cover-teal {
    left: 456px; top: 360px; width: 204px; height: 140px;
    background: linear-gradient(180deg, var(--teal-deep), var(--teal));
  }
  .cover-stripe { left: 456px; top: 182px; width: 204px; height: 22px; background: var(--aqua); opacity: 0.8; }
  .cover-title { left: 462px; top: 22px; font-size: 19.5px; font-weight: 700; line-height: 0.98; color: var(--heading); }
  .cover-title .accent { color: var(--teal); }
  .sticker {
    left: 454px; top: 116px; width: 92px; height: 92px; border-radius: 50%;
    background: radial-gradient(circle at 40% 35%, #2aa3ad, var(--teal-deep) 70%);
    border: 3px solid var(--white);
    color: var(--white); text-align: center; padding-top: 26px;
  }
  .sticker .lead { display: block; font-size: 10px; font-weight: 700; font-style: italic; }
  .sticker .year { display: block; font-size: 21px; font-weight: 700; line-height: 1; }
  .bogof { left: 550px; top: 134px; font-size: 16.5px; font-weight: 700; line-height: 1; color: var(--ink); }
  .photo-board {
    left: 461px; top: 206px; width: 184px; height: 214px;
    background: linear-gradient(160deg, #f5f6f7 0%, #dfe3e6 40%, #9aa6b2 70%, #e9ecee 100%);
  }
  .cover-offer { left: 460px; top: 436px; width: 190px; font-size: 10px; line-height: 1.2; color: var(--white); }
</style>
</head>
<body>

<section class="spread spread--inside" aria-label="Inside pages">
  <div class="streak"></div>
  <div class="column-wash"></div>

  <h2 class="abs site-title">OakleighOnline.com</h2>
  <p class="abs site-sub">great for branding<br>and attracting new contacts</p>
  <div class="abs rule" style="left:24px;top:111px;width:170px"></div>
  <div class="abs body-copy" style="left:24px;top:135px">
    <p>OakleighOnline.com is local community website packed with a range of great features from local news and weather forecasts to daily horoscopes and competitions. One of the most popular features of the site is the business directory which is frequently used by visitors as a tool for finding local businesses.</p>
    <p style="margin-top:9px">Our directory listings also help with external link building and, in their own right, achieve high positions in the Search Engines. Oakleigh Online is part of a network of 80 websites which cover the majority of the main towns and cities across the UK.</p>
  </div>

  <p class="abs seo-title">Increase traffic<br>to your website using <strong>SEO</strong></p>
  <div class="abs rule" style="left:24px;top:339px;width:170px"></div>
  <div class="abs body-copy" style="left:24px;top:358px">
    <p>SEO (Search Engine Optimisation) is the process of improving a websites position in the Search Engines for a relevant keyword.</p>
    <p style="margin-top:9px">A constant Search Engine Optimisation (SEO) process is crucial if you want your web site to be found by search engines and be on page one for your respective keywords.</p>
  </div>

  <h2 class="abs panel-title" style="left:237px;top:62px">Improve your branding?</h2>
  <p class="abs item-title">3. Increased brand exposure</p>
  <p class="abs body-copy" style="left:456px;top:80px;width:180px">Your company branding will be displayed across OakleighOnline.com which will be seen by thousands of people each month.</p>
</section>

<section class="spread spread--outside" aria-label="Outside pages">
  <div class="streak streak--right"></div>

  <h2 class="abs value-title">Great Value for Money</h2>
  <div class="abs value-copy">
    <p>We are offering all of the above for only £180 per month, subject to a 12 month contract, making this one of the most cost effective Internet Marketing packages in the UK.</p>
    <p>For more information please call</p>
    <p>Brandon Vale Internet Solutions on</p>
    <p class="contact">08000 41 73 29<br>or email info@brandonvale.net.</p>
  </div>
  <div class="abs photo-pen" role="img" aria-label="Photo of a businessman drawing a rising chart line with a marker"></div>

  <div class="abs teal-band"></div>
  <p class="abs band-lead">Attract more new customers by promoting your website in two great ways.</p>
  <p class="abs band-small">Take advantage of our cost effective Internet Marketing package where you will receive coverage across your local 'Onlines' directories as well as a professional Search Engine Optimisation package.</p>
  <p class="abs band-note">Please note that<br>increased traffic to your website is<br>normally experienced after month three.<span class="ask">Guarentee?</span></p>

  <div class="abs cover-teal"></div>
  <div class="abs cover-stripe"></div>
  <h1 class="abs cover-title">Would you like<br>to attract more<br><span class="accent">customers</span><br>to your business?</h1>
  <div class="abs photo-board" role="img" aria-label="Photo of a businessman presenting a growth chart on a whiteboard in a meeting"></div>
  <div class="abs sticker"><span class="lead">Special offer for</span><span class="year">2011</span></div>
  <p class="abs bogof">Buy one<br>Get one free!</p>
  <p class="abs cover-offer">Buy our Business Foundation SEO package and get an advert on 'OakleighOnline.com' for free!</p>
</section>

</body>
</html>
```